Wordpress Design for Martin Halvorsen | Quiet Resolve

Summary
I am accepting designs concepts for my personal blog and web presence – http://www.martinhalvorsen.com. The Blog, subtitled “Quiet Resolve”, provides a platform upon which I have established a personal brand and market my services as an board member, executive advisor, public speaker, and thought leader.
The successful design will balance an executive and professional design with a bit of innovation and passion. It will match the style and colors of the logo provided and adhere to the requirements listed below while providing a visually creative, appealing, and user-engaging experience.
A few blogs that I consider to be well designed and similar in content to what I’m looking for include:
• http://peterlundgrave.com (by far the best representation)
• http://pinecrestwriter.com/
• http://www.karlbrenner.com/
Technical Requirements
The design must be implementable in WordPress using “Plainframe Theme” (http://plainframetheme.com/). Customizations to Plainframe Theme are allowed, but should not be extraordinary.
The design must be implementable using clean and standard html/css techniques.
The design must include a standard header that leverages the attached logo
The design must include a search engine optimized footer layout that includes various links. The footer must include a series of small print links include a permission policy and a privacy policy.
The design must include placeholders for advertisements on each page. Any standard Google Adwords sizes are acceptable.
The design must include a standard site template/shell and at least 3 internal page designs.
Designs should be submitted for (at minimum) the following pages (detailed below):
• Home
• About
• Boards and/or Speaking pages
Information Architecture
Primary Navigation / Pages
Home
The home page will be primarily comprised of blog content. A layout and design is required for each of the following blog types:
• Standard – a typical weblog comprised of text and graphics
• Quote – a short snippet which includes a sentence and an attribution
• Video Blog – a video surrounded by
• Podcast
• Image – an image only (with caption) blog
Each blog post should contain social actions – the ability to tweet, share, etc. . .with the click of a button.
In addition to the core content, the home page should provide a brief introduction and standard picture and/or video. Other optional elements may include a tag cloud, search box, etc. . .use your creativity
About
Contains basic “about me” information. This page will serve as a template for all other “standard” pages. Please include the basic elements for a website in this page. These should include:
• A minimum of 3 Headings - H1, H2, and H3
• A bulleted list
• A numbered list
• A table
• An image
• A call to action (typically an image/button)
Boards
A special page dedicated to the boards I sit on and organizations I serve. There should be two sections – one for current board positions and one for previous positions. Each position should contain a logo, company name, and short description.
I imagine the organizations logo being in full color for the current positions but grey scale for the previous, but that’s just an idea, not a requirement.
Speaking
A special page dedicated to previous and upcoming speaking engagements. The layout may be similar to the Board page. No need to submit a separate layout for it unless you believe they should be different. Each speaking engagement will include a logo, event name, and short description as well as a date/time and whether it’s open to the public or not.
Contact
No need for a separate layout unless desired.
Other Elements
The Blog should provide quick access to the following blog “categories”:
• Business and Entrepreneurship
• Leadership and Inspiration
• Innovation and Technology
• Faith and Family
The template should include prominent links to each of my social media pages:
• Twitter
• LinkedIn
• YouTube
• Facebook
• Google+
The template should include a link to the blog archives
Target Market(s)
Executives, business people
Industry/Entity Type
Business
Look and feel
Each slider illustrates characteristics of the customer's brand and the style your logo design should communicate.

```html
<!DOCTYPE html>
<html lang="en">
<head>
<meta charset="utf-8">
<title>Martin Halvorsen | Quiet Resolve</title>
<link href="https://fonts.googleapis.com/css2?family=Arimo:wght@400;700&family=Nunito:wght@700;800&display=swap" rel="stylesheet">
<style>
:root{
  --blue:#1a9ad6;
  --sky:#4ec3f0;
  --sky-deep:#2bb3e8;
  --ink:#333;
  --muted:#666;
  --page:#f1f1f1;
  --card:#fff;
  --line:#dcdcdc;
  --red:#b8261b;
  --orange:#f28c00;
  --footer:#6a6a6a;
}
*{box-sizing:border-box;margin:0;padding:0}
html,body{width:674px;height:1200px;overflow:hidden}
body{position:relative;background:var(--page);font-family:"Arimo",Arial,sans-serif;color:var(--ink)}
a{color:inherit;text-decoration:none}
.abs{position:absolute}
.topbar{left:0;top:0;width:674px;height:9px;background:#666}
.header{left:0;top:9px;width:674px;height:116px;background:linear-gradient(#fff 40%,#ececec)}
.brand{left:20px;top:40px;display:flex;align-items:center;gap:10px}
.brand-mark{width:34px;height:34px;background:var(--blue)}
.brand-name{font-family:"Nunito",sans-serif;font-weight:800;font-size:29px;color:var(--blue);line-height:1}
.tagline{left:132px;top:70px;font-size:10px;letter-spacing:4.2px;color:#8a8a8a;font-weight:700}
.social{left:522px;top:21px;display:flex;gap:7px}
.social span{width:19px;height:19px;border-radius:3px;display:block}
.search{left:523px;top:50px;width:134px;height:17px;border:1px solid #bbb;border-radius:3px;background:#fff;font-size:8px;padding:3px 8px;color:#555}
.search svg{position:absolute;right:4px;top:2px}
.nav{right:17px;top:80px;font-size:9px;color:#444;display:flex;gap:7px}
.nav i{font-style:normal;color:#999}
.tabs{left:292px;top:106px;display:flex;gap:3px}
.tabs a{height:19px;font-size:9px;color:#123;display:flex;align-items:center;justify-content:center;border-radius:4px 4px 0 0;background:linear-gradient(#36b8ec,var(--sky-deep))}
.tabs a.on{background:linear-gradient(#7fd6f6,#49c0ee)}
.hero{left:0;top:125px;width:674px;height:251px;background:linear-gradient(var(--sky),#3db7ea)}
.slide{left:18px;top:141px;width:403px;height:216px;background:#fff;padding:4px;box-shadow:0 4px 6px rgba(0,0,0,.35)}
.slide div{width:100%;height:100%;background:linear-gradient(#3d5a2e,#5f8a45 45%,#d9d9d9 75%,#a9b0a0)}
.arrow{width:23px;height:23px;border-radius:50%;background:#fff;font-size:14px;font-weight:700;display:flex;align-items:center;justify-content:center;color:#333}
.subscribe{left:437px;top:141px;width:221px;height:76px;background:#fff;border-radius:5px;padding:10px 12px}
.subscribe h3{font-weight:400;font-size:12px;letter-spacing:.5px;color:#333;margin-bottom:10px}
.sub-row{display:flex;gap:6px}
.sub-row span{flex:1;height:22px;border:1px solid #ddd;border-radius:3px;font-size:7px;color:#888;padding:7px 8px}
.sub-row b{width:72px;height:22px;background:var(--orange);color:#fff;font-size:9px;font-weight:400;display:flex;align-items:center;justify-content:center;border-radius:2px}
.video{left:437px;top:230px;width:221px;height:127px;background:#111;padding:5px}
.video-screen{width:100%;height:97px;background:linear-gradient(90deg,#e6e6e6,#d0d0d0 60%,#7a7f88);position:relative}
.video-screen p{position:absolute;left:25px;top:35px;font-size:11px;color:#333}
.play{position:absolute;left:92px;top:50px;width:20px;height:15px;background:#222;border-radius:3px}
.play:after{content:"";position:absolute;left:7px;top:4px;border-left:7px solid #fff;border-top:4px solid transparent;border-bottom:4px solid transparent}
.controls{height:20px;display:flex;align-items:center;gap:12px;padding:0 8px;color:#aaa;font-size:7px}
.post{left:15px;width:440px;background:linear-gradient(#fff 55%,#ececec);border:1px solid var(--line);border-radius:4px;padding:14px 14px 0}
.post h2{font-weight:400;font-size:12.5px;color:var(--blue);letter-spacing:.3px}
.meta{font-size:8px;color:#444;margin-top:8px}
.meta em{font-style:normal;color:var(--blue)}
.body{display:flex;gap:14px;margin-top:16px}
.thumb{flex:none}
.body p{font-size:8.3px;line-height:14.5px;color:#444;margin-bottom:10px}
.more{position:absolute;right:15px;font-size:8px;color:var(--red)}
.widget{left:466px;width:197px;background:#fff;border:1px solid var(--line);border-radius:4px}
.widget h3{font-weight:400;font-size:12px;color:var(--blue);margin:12px 9px 0;padding-bottom:6px;border-bottom:1px dotted #aaa}
.cloud{padding:10px 9px;line-height:24px;color:#333;font-size:8px}
.cloud .m{font-size:11px}.cloud .l{font-size:12px}.cloud .xl{font-size:16px}
.ad{left:467px;top:852px;width:196px;height:169px;background:linear-gradient(#333,#222);color:#fff;text-align:center}
.ad p{font-size:17px;margin-top:14px}
.ad .ad-name{font-size:22px;font-weight:700;letter-spacing:1px;margin-top:46px}
.ad .btn{display:block;margin:14px 12px 0;height:25px;background:linear-gradient(#5fb0ea,#2f85d2);border-radius:3px;font-size:14px;font-weight:700;line-height:25px}
.ad .stripe{position:absolute;left:0;bottom:0;width:100%;height:3px;background:linear-gradient(90deg,#e33 25%,#f90 25% 50%,#3b6 50% 75%,#39f 75%)}
.pager{top:1095px;left:212px;display:flex;gap:5px}
.pager span{width:16px;height:15px;background:#555;color:#fff;font-size:7.5px;border-radius:3px;display:flex;align-items:center;justify-content:center}
.footer{left:0;top:1127px;width:674px;height:73px;background:var(--footer);color:#fff;font-size:7.5px;text-align:center}
.footer p{margin-top:12px}
.footer p i{font-style:normal;margin:0 7px}
</style>
</head>
<body>
<div class="abs topbar"></div>
<header class="abs header"></header>
<div class="abs brand"><span class="brand-mark"></span><span class="brand-name">Martin Halvorsen</span></div>
<div class="abs tagline">QUIET RESOLVE</div>
<div class="abs social" aria-label="Social profiles">
  <span style="background:#c4302b"></span><span style="background:#1a7ab8"></span><span style="background:#3b5998"></span><span style="background:#3fb6e6"></span><span style="background:#f0860f"></span>
</div>
<div class="abs search">Search
  <svg width="11" height="11" viewBox="0 0 11 11"><circle cx="4.5" cy="4.5" r="3.3" fill="none" stroke="#888" stroke-width="1.3"/><line x1="7" y1="7" x2="10" y2="10" stroke="#888" stroke-width="1.5"/></svg>
</div>
<nav class="abs nav"><a>Home</a><i>|</i><a>About</a><i>|</i><a>Reading List</a><i>|</i><a>Speaking</a><i>|</i><a>Archives</a><i>|</i><a>Contact</a></nav>
<div class="abs tabs">
  <a class="on" style="width:99px">Entrepreneurship</a><a style="width:85px">Leadership</a><a style="width:85px">Innovation</a><a style="width:99px">Faith and Family</a>
</div>

<section class="abs hero"></section>
<div class="abs slide"><div role="img" aria-label="Family portrait seated on a blanket in a park"></div></div>
<div class="abs arrow" style="left:14px;top:236px">»</div>
<div class="abs arrow" style="left:405px;top:236px">«</div>
<div class="abs subscribe">
  <h3>Subscribe</h3>
  <div class="sub-row"><span>Enter Your Email Adress</span><b>Subscribe</b></div>
</div>
<div class="abs video">
  <div class="video-screen" role="img" aria-label="Video still of Martin Halvorsen in a suit">
    <p>Martin Halvorsen</p><span class="play"></span>
  </div>
  <div class="controls"><span>❚❚</span><span>◀)</span><span>0:00 / 1:10</span></div>
</div>

<article class="abs post" style="top:395px;height:218px">
  <h2>CONSUMERIZATION MEETS MOBILE</h2>
  <div class="meta">April 4, 2012 in Innovation with <em>0 Comments</em></div>
  <div class="body">
    <div class="thumb" role="img" aria-label="Touchscreen mobile phone" style="width:140px;height:95px;background:linear-gradient(160deg,#555,#1a1a1a 60%,#777);border-radius:8px;margin-top:8px"></div>
    <div style="padding-left:6px"><p>Over the course of the past couple of years, the trend towards a more consumer oriented approach to enterprise IT has gained significant play in the industry.  Significant discussion has ensued about how this “consumerization” has changed the way that IT assets are purchased.</p><p>Mobile products are pushing the consumerization trend forward. There are several reasons why Mobile lends itself to a more consumer oriented buying cycle.</p></div>
  </div>
  <a class="more" style="top:193px">Continue Reading...</a>
</article>

<article class="abs post" style="top:625px;height:218px">
  <h2>THE BEST REWARD YET</h2>
  <div class="meta">April 4, 2012 in Leadership with <em>0 Comments</em></div>
  <div class="body">
    <div class="thumb" role="img" aria-label="Portrait photo of a man in a suit" style="width:95px;height:140px;background:linear-gradient(#8a8a8a,#555 60%,#2a2a30);border:2px solid #fff;box-shadow:0 0 2px #999"></div>
    <div><p>I don’t typically post self-acolades but today I was humbled to receive perhaps the best recognition I could have ever hoped for.  It’s a reflection of the culture we’ve built here at Northgate Works and it’s a tribute to our team who has taken the humble idea that the dignity of the worker is worth fighting for and made it a reality.</p><p>One of our teammates has been out for a while and here is a piece of her response to my email checking in on her:</p></div>
  </div>
  <a class="more" style="top:186px">Continue Reading...</a>
</article>

<article class="abs post" style="top:861px;height:218px">
  <h2>WHEN CONSENSUS GETS IN THE WAY</h2>
  <div class="meta">April 4, 2012 in Leadership with <em>0 Comments</em></div>
  <div class="body">
    <div class="thumb" role="img" aria-label="Illustration of a red figure stepping ahead of a grey group" style="width:140px;height:130px;background:linear-gradient(90deg,#e4e4e4,#c9c9c9 55%,#e03a2a 70%,#c62218)"></div>
    <div style="padding-left:2px"><p>In my last post I outlined the power of consensus building.  Consensus building is an important tool for making informed decisions and promoting organizational buy-in.  Strong consensus builders tend to build strong, motivated, teams.</p><p>As with all leadership tools (and most things in life), one size does not fit all situations.  Sometimes the unanimity required to attain consensus is impossible to attain as holdouts dig in their heels.</p></div>
  </div>
  <a class="more" style="top:193px">Continue Reading...</a>
</article>

<aside class="abs widget" style="top:394px;height:280px">
  <h3>POPULAR TOPICS</h3>
  <div class="cloud">balance blog <span class="xl">business</span> catholic cloud communication <span class="l">culture</span> <span class="l">dignity</span> of the worker friendship funding <span class="l">growth</span> hiring holiday <span class="l">integrity</span> <span class="l">management</span> <span class="l">marriage</span> <span class="l">media</span> mentor mobile outsourcing passion pictures <span class="l">politics</span> <span class="l">product</span> productivity <span class="m">public speaking</span> scaffolding <span class="l">speaking</span> <span class="m">startup</span> strategy <span class="l">teamwork</span> <span class="m">trust</span> purpose travel virtue</div>
</aside>
<div class="abs widget" style="top:692px;height:147px;padding:3px">
  <div role="img" aria-label="Extended family group photo on a wooden bridge" style="height:100%;background:linear-gradient(#5f8a45,#8fb56d 45%,#e8e8e8 65%,#8a6a45)"></div>
</div>
<div class="abs ad">
  <p>Hear Us On</p>
  <div class="ad-name">TUNEWAVE</div>
  <span class="btn">Get It Now ▸</span>
  <span class="stripe"></span>
</div>

<div class="abs pager"><span>1</span><span>2</span><span>3</span><span>4</span><span style="margin-left:54px">10</span></div>

<footer class="abs footer">
  <p>Home<i>|</i>About<i>|</i>Reading List<i>|</i>Speaking<i>|</i>Archives<i>|</i>Contact</p>
  <p>Entrepreneurship<i>|</i>Leadership<i>|</i>Innovation<i>|</i>Faith and Family</p>
  <p>© 2012 Martin Halvorsen, All Rights Reserved</p>
</footer>
</body>
</html>
```